Brenwick Holdings Limited
BrenHold
I agree with jonwel. The logo's resolution is too low. Please provide an Adobe Illustrator File or a larger logo. Thanks.
#7 obviously doesn't get the fact that this is a business card, not a logo. :-)
H! GT please provide eps or ai files for the logo, the png file is too small and not a transparent.. Thanks!

```html
<!DOCTYPE html>
<html lang="en">
<head>
<meta charset="utf-8">
<title>Brenwick Holdings Stationery</title>
<link rel="stylesheet" href="https://fonts.googleapis.com/css2?family=Arimo:wght@400;700&display=swap">
<style>
:root{
  --backdrop:#3b1713;
  --paper:#ffffff;
  --ink:#4a4a4a;
  --ink-soft:#6b6b6b;
  --brand-grey:#6d6e71;
  --brand-blue:#1f6fb8;
  --faint:#ececec;
  --label:#ffffff;
}
*{box-sizing:border-box;margin:0;padding:0}
html,body{width:1200px;height:931px;overflow:hidden}
body{background:var(--backdrop);font-family:"Arimo",Arial,sans-serif;color:var(--ink);position:relative}
.label{position:absolute;color:var(--label);font-size:14px;font-weight:700;display:flex;align-items:center;gap:6px}
.label::before{content:"";border-left:6px solid transparent;border-right:6px solid transparent;border-top:8px solid var(--label)}
.label--letterhead{left:764px;top:80px}
.label--bizcard{left:1032px;top:410px}

.letterhead{position:absolute;left:25px;top:102px;width:841px;height:840px;background:var(--paper);overflow:hidden;box-shadow:0 4px 14px rgba(0,0,0,.4)}
.bizcard{position:absolute;left:557px;top:434px;width:568px;height:377px;background:var(--paper);overflow:hidden;box-shadow:-6px 10px 24px rgba(0,0,0,.45)}

.brand{display:flex;flex-direction:column;align-items:flex-start}
.brand__row{display:flex;align-items:center;gap:12px}
.brand__mark{background:var(--brand-blue);flex:none}
.brand__name{font-weight:400;color:var(--brand-grey);line-height:1}
.brand__tagline{color:var(--brand-blue);font-weight:400}

.letterhead .brand{position:absolute;left:80px;top:40px}
.letterhead .brand__mark{width:30px;height:30px}
.letterhead .brand__name{font-size:60px;letter-spacing:1px}
.letterhead .brand__tagline{font-size:15px;margin:8px 0 0 44px}

.contacts{list-style:none;font-size:13px;line-height:21px;color:var(--ink)}
.contacts li{display:flex;align-items:center;gap:7px}
.contacts svg{width:13px;height:13px;flex:none}
.letterhead .contacts{position:absolute;left:468px;top:92px}

.address{font-style:normal;font-size:13px;line-height:21px;color:var(--ink-soft)}
.address strong{color:var(--ink);font-weight:700}
.letterhead .address{position:absolute;left:660px;top:68px}

.site-vertical{position:absolute;left:58px;bottom:40px;transform:rotate(-90deg);transform-origin:left bottom;font-size:14px;font-weight:700;letter-spacing:6px;color:var(--brand-blue);white-space:nowrap;translate:20px 0}

.bizcard .brand{position:absolute;left:28px;top:42px;align-items:center}
.bizcard .brand__mark{width:22px;height:22px}
.bizcard .brand__name{font-size:46px}
.bizcard .brand__tagline{font-size:12px;margin-top:6px}

.person{position:absolute;left:350px;top:100px}
.person__name{font-size:14px;font-weight:700;color:var(--brand-blue);letter-spacing:.5px}
.person__role{font-size:12px;font-style:italic;color:var(--ink-soft);margin-top:3px}
.bizcard .address{position:absolute;left:350px;top:162px;font-size:12px;line-height:18px}
.bizcard .contacts{position:absolute;left:155px;top:190px;font-size:12px;line-height:19px}
.bizcard .site{position:absolute;left:158px;top:280px;font-size:12px;font-weight:700;color:var(--brand-blue)}

.watermark{position:absolute;display:flex;align-items:center;gap:14px;color:var(--faint);font-weight:400;line-height:1;white-space:nowrap}
.watermark__mark{border:6px solid var(--faint);flex:none}
.letterhead .watermark{left:600px;top:720px;font-size:110px}
.letterhead .watermark__mark{width:70px;height:70px}
.bizcard .watermark{left:440px;top:290px;font-size:78px}
.bizcard .watermark__mark{width:50px;height:50px}
</style>
</head>
<body>
<svg width="0" height="0" style="position:absolute">
  <defs>
    <symbol id="icon-phone" viewBox="0 0 16 16"><circle cx="8" cy="8" r="8" fill="#1f6fb8"/><path d="M5 4.5l1.6-.3.8 2-1 .8a6 6 0 002.6 2.6l.8-1 2 .8-.3 1.6c-3.8.2-6.7-2.7-6.5-6.5z" fill="#fff"/></symbol>
    <symbol id="icon-mobile" viewBox="0 0 16 16"><circle cx="8" cy="8" r="8" fill="#1f6fb8"/><rect x="5.5" y="3.5" width="5" height="9" rx="1" fill="#fff"/><rect x="6.5" y="4.8" width="3" height="5.2" fill="#1f6fb8"/></symbol>
    <symbol id="icon-fax" viewBox="0 0 16 16"><circle cx="8" cy="8" r="8" fill="#1f6fb8"/><rect x="4" y="6.5" width="8" height="5" fill="#fff"/><rect x="5.5" y="4" width="5" height="3" fill="#fff"/></symbol>
    <symbol id="icon-mail" viewBox="0 0 16 16"><circle cx="8" cy="8" r="8" fill="#1f6fb8"/><rect x="4" y="5" width="8" height="6" fill="#fff"/><path d="M4 5l4 3.5L12 5" stroke="#1f6fb8" fill="none"/></symbol>
  </defs>
</svg>

<div class="label label--letterhead">Letterhead</div>
<div class="label label--bizcard">Bizcard</div>

<section class="letterhead">
  <div class="brand">
    <div class="brand__row"><span class="brand__mark"></span><span class="brand__name">BrenHold</span></div>
    <span class="brand__tagline">Investing in Technology</span>
  </div>
  <ul class="contacts">
    <li><svg><use href="#icon-phone"/></svg>+44 208 555 0142</li>
    <li><svg><use href="#icon-mobile"/></svg>+44 7700 900318</li>
    <li><svg><use href="#icon-fax"/></svg>+44 208 555 0187</li>
    <li><svg><use href="#icon-mail"/></svg>tom.vale@brenhold.co.uk</li>
  </ul>
  <address class="address">
    <strong>Brenwick Holdings Limited</strong><br>
    Harbour Court<br>Fenwick Road<br>Elmsford<br>Northshire<br>EL4 7QX
  </address>
  <div class="watermark"><span class="watermark__mark"></span>BrenHold</div>
  <div class="site-vertical">www.brenhold.co.uk</div>
</section>

<section class="bizcard">
  <div class="brand">
    <div class="brand__row"><span class="brand__mark"></span><span class="brand__name">BrenHold</span></div>
    <span class="brand__tagline">Investing in Technology</span>
  </div>
  <div class="person">
    <div class="person__name">TOM C VALE</div>
    <div class="person__role">Chief Executive</div>
  </div>
  <address class="address">
    <strong>Brenwick Holdings Limited</strong><br>
    Harbour Court<br>Fenwick Road<br>Elmsford<br>Northshire<br>EL4 7QX
  </address>
  <ul class="contacts">
    <li><svg><use href="#icon-phone"/></svg>+44 208 555 0142</li>
    <li><svg><use href="#icon-mobile"/></svg>+44 7700 900318</li>
    <li><svg><use href="#icon-fax"/></svg>+44 208 555 0187</li>
    <li><svg><use href="#icon-mail"/></svg>tom.vale@brenhold.co.uk</li>
  </ul>
  <div class="site">www.brenhold.co.uk</div>
  <div class="watermark"><span class="watermark__mark"></span>BrenHold</div>
</section>
</body>
</html>
```